Stanbrook Fire Services Pty Ltd

We need business cards for a company based in Perth, we install, service and maintain fire equipment.
On the front we want a great design with our logo and a small spot for our full company name, general company email address and office number. On the back we need space for our name, title, mobile number and email address on the back.

Target Market(s)

Facility managers and commercial/industrial building owners/occupiers.

Contact Information for Business Card

Font styles to use
Sans Serif

Requirements
Must have
• Please only submit 5 of your best samples.
Darker tones are preferred.
Nice to have
• We want to use, black, red and grey. Keep it modern and clean.
I've attached the company logo and a sample of a boarder we use on our emergency plans.
Should not have
• No preference. Let the designer choose.

```html
<!DOCTYPE html>
<html lang="en">
<head>
<meta charset="utf-8">
<title>Stanbrook Fire Services – Business Cards</title>
<link href="https://fonts.googleapis.com/css2?family=Arimo:wght@400;700&display=swap" rel="stylesheet">
<style>
  :root {
    --page: #2a2a2a;
    --card: #0b0b0b;
    --red: #e3202a;
    --silver: #d6d6d6;
    --grey: #b5b5b5;
    --divider: #3a3a3a;
  }
  * { margin: 0; padding: 0; box-sizing: border-box; }
  html, body {
    width: 1200px; height: 900px; overflow: hidden;
    background: var(--page);
    font-family: "Arimo", Arial, sans-serif;
  }
  .stage { position: relative; width: 1200px; height: 900px; }
  .card {
    position: absolute;
    width: 525px; height: 300px;
    background: var(--card);
    border-radius: 22px;
    display: flex; align-items: center;
  }
  .card--person { left: 70px; top: 500px; }
  .card--company { left: 605px; top: 100px; }

  .brand {
    width: 270px;
    display: flex; justify-content: center; align-items: center; gap: 10px;
    font-weight: 700; font-size: 30px; letter-spacing: 1px;
  }
  .brand__dot { width: 12px; height: 12px; }
  .card--person .brand { color: var(--red); }
  .card--person .brand__dot { background: var(--red); }
  .card--company .brand { color: var(--silver); }
  .card--company .brand__dot { background: var(--silver); }

  .divider { width: 1px; height: 96px; background: var(--divider); }

  .details { padding-left: 30px; }
  .details__name { color: var(--red); font-weight: 700; font-size: 17px; text-transform: uppercase; }
  .details__title { color: var(--grey); font-size: 14px; margin-bottom: 20px; }
  .details__company { color: var(--silver); font-weight: 700; font-size: 16px; line-height: 1.15; text-transform: uppercase; margin-bottom: 6px; }
  .details__office { color: var(--silver); font-weight: 700; font-size: 18px; margin-bottom: 6px; }
  .contact { display: flex; align-items: center; gap: 8px; font-size: 13px; line-height: 1.55; }
  .card--person .contact { color: var(--grey); }
  .card--company .contact { color: var(--silver); font-size: 12px; }
  .contact svg { width: 12px; height: 12px; flex: none; }
</style>
</head>
<body>
<div class="stage">

  <section class="card card--company">
    <div class="brand"><span class="brand__dot"></span>STANBROOK</div>
    <div class="divider"></div>
    <div class="details">
      <p class="details__company">Stanbrook Fire<br>Services Pty Ltd</p>
      <p class="details__office">555.0190.0190</p>
      <p class="contact">
        <svg viewBox="0 0 12 12"><rect x="0.5" y="2.5" width="11" height="7" fill="none" stroke="#d6d6d6"/><path d="M0.5 2.5 6 7 11.5 2.5" fill="none" stroke="#d6d6d6"/></svg>
        info@stanbrookfs.com
      </p>
      <p class="contact">
        <svg viewBox="0 0 12 12"><circle cx="6" cy="6" r="5.3" fill="none" stroke="#d6d6d6"/><ellipse cx="6" cy="6" rx="2.3" ry="5.3" fill="none" stroke="#d6d6d6"/><path d="M0.7 6h10.6" stroke="#d6d6d6"/></svg>
        www.stanbrookfs.com
      </p>
    </div>
  </section>

  <section class="card card--person">
    <div class="brand"><span class="brand__dot"></span>STANBROOK</div>
    <div class="divider"></div>
    <div class="details">
      <p class="details__name">Marcus Hale</p>
      <p class="details__title">Managing Director</p>
      <p class="contact">
        <svg viewBox="0 0 12 12"><rect x="3" y="0.5" width="6" height="11" rx="1" fill="none" stroke="#e3202a"/><path d="M5 9.5h2" stroke="#e3202a"/></svg>
        555.0142.0142
      </p>
      <p class="contact">
        <svg viewBox="0 0 12 12"><rect x="0.5" y="2.5" width="11" height="7" fill="#e3202a"/><path d="M0.5 2.5 6 7 11.5 2.5" fill="none" stroke="#0b0b0b"/></svg>
        m.hale@stanbrookfs.com
      </p>
    </div>
  </section>

</div>
</body>
</html>
```